KORBLE Development is an idea development firm. This business card is for Weekend Wicket League, a site that allows users from all over the world to play fantasy cricket against each other.
We need a business card for WWL using our logo and its associated colors. The cards are for the two founders, Tobias Whitlow and Martin Dobrescu. We would like our own cards.
We are handing our card to potential investors and sponsors of our site. It needs to be unique (like our brand.)
Updates
I wanted to thank everyone for their awesome designs!!! It was a hard choice - we narrowed it down to 7 then to three then to 1. All of you are extremely talented - THANK YOU.
Target Market(s)
Potential Investors, Partners
Industry/Entity Type
Business
Contact Information for Business Card
Korble Development : Weekend Wicket League
Tobias Whitlow
Founder
555-204-7316
tobias@korble.example
www.weekendwicketleague.example
....
Martin Dobrescu
Founder
555-871-0492
martin@korble.example
Look and feel

```html
<!DOCTYPE html>
<html lang="en">
<head>
<meta charset="utf-8">
<title>Weekend Wicket League – Business Card</title>
<link rel="stylesheet" href="https://fonts.googleapis.com/css2?family=Crimson+Text:wght@400;700&display=swap">
<style>
  :root {
    --page-bg: #ecebe8;
    --card-white: #ffffff;
    --green-deep: #22803e;
    --green-mid: #2e8b45;
    --green-glow: #7cc04a;
    --lime: #9acd3c;
    --ink: #1a1a1a;
    --watermark: #e6e6e6;
    --logo-white: #ffffff;
  }
  * { margin: 0; padding: 0; box-sizing: border-box; }
  html, body {
    width: 1200px; height: 1200px; overflow: hidden;
    background: var(--page-bg);
    font-family: "Crimson Text", Georgia, serif;
    color: var(--ink);
  }
  .sheet {
    position: relative; width: 1200px; height: 1200px;
  }
  .card {
    position: absolute; left: 160px; width: 880px; height: 500px;
    overflow: hidden;
    box-shadow: 0 6px 18px rgba(0,0,0,0.18);
  }
  /* Back side */
  .card-back {
    top: 70px;
    background: radial-gradient(circle at 45% 42%, var(--green-glow) 0%, #4ea243 18%, var(--green-mid) 42%, var(--green-deep) 100%);
  }
  .card-back .accent-stripe {
    position: absolute; left: 0; right: 0; top: 372px; height: 36px;
    background: var(--lime);
  }
  .card-back .brand-mark {
    position: absolute; left: 396px; top: 170px; width: 0;
    display: flex; flex-direction: column; align-items: center;
  }
  .brand-mark .mark-circle {
    width: 44px; height: 44px; border-radius: 50%;
    background: var(--logo-white); margin-bottom: 12px;
  }
  .brand-mark .brand-name {
    white-space: nowrap; text-align: center;
    font-weight: 400; font-size: 21px; line-height: 1.15;
    color: var(--logo-white);
  }
  /* Front side */
  .card-front {
    top: 630px; background: var(--card-white);
  }
  .card-front .base-band {
    position: absolute; left: 0; right: 0; bottom: 0; height: 62px;
    background: var(--green-mid);
  }
  .card-front .watermark {
    position: absolute; left: 70px; top: 80px;
    display: flex; flex-direction: column; align-items: center;
    color: var(--watermark);
  }
  .watermark .mark-circle {
    width: 150px; height: 150px; border-radius: 50%;
    background: var(--watermark); margin-bottom: 14px;
  }
  .watermark .brand-name {
    font-weight: 700; font-size: 26px; white-space: nowrap;
  }
  .contact-block {
    position: absolute; left: 400px; right: 30px;
  }
  .contact-block .firm {
    font-weight: 700; font-size: 26px; line-height: 1;
  }
  .contact-block .details {
    font-size: 15px; line-height: 1.3; margin-top: 3px;
  }
  .founder-one { top: 70px; }
  .founder-two { top: 170px; }
  .web-block {
    position: absolute; left: 400px; top: 330px;
    font-size: 14px; line-height: 1.15;
  }
</style>
</head>
<body>
<main class="sheet">
  <section class="card card-back" aria-label="Card back">
    <div class="brand-mark">
      <span class="mark-circle"></span>
      <span class="brand-name">Weekend Wicket<br>League</span>
    </div>
    <div class="accent-stripe"></div>
  </section>

  <section class="card card-front" aria-label="Card front">
    <div class="watermark" aria-hidden="true">
      <span class="mark-circle"></span>
      <span class="brand-name">Weekend Wicket League</span>
    </div>

    <div class="contact-block founder-one">
      <p class="firm">Korble Development</p>
      <p class="details">Weekend Wicket League Tobias Whitlow Founder 555-204-7316</p>
    </div>

    <div class="contact-block founder-two">
      <p class="firm">Korble Development</p>
      <p class="details">Weekend Wicket League Martin Dobrescu Founder 555-871-0492</p>
    </div>

    <div class="web-block">
      <p>tobias@korble.example www.weekendwicketleague.example</p>
      <p>martin@korble.example</p>
      <p>www.weekendwicketleague.example</p>
    </div>

    <div class="base-band"></div>
  </section>
</main>
</body>
</html>
```